Professional Photography Business cards

I need business cards that include my logo which I have uploaded. I run a photography business. I am open to ideas but I would like one side to have my logo and the other side to have my contact info. I don't have a website made but I do own a website domain. I have uploaded 2 different logo color schemes. My business colors are Blue, black , and white.

Business Name
Business Phone Number
Business Email
Business Website address
Instagram

Industry/Entity Type

Professional Photography

Contact Information for Business Card

Phone Number: 555-314-8027 email: info@tkellan-studios.example Instagram: @t.kellanstudios website doman- www.tkellan-studios.example

Requirements
Must have
• I like the idea of a business card with a full black background front and back of card. My colors must include royal blue, black, and white

```html
<!DOCTYPE html>
<html lang="en">
<head>
<meta charset="utf-8">
<title>T. Kellan Studios — Business Card</title>
<link rel="stylesheet" href="https://fonts.googleapis.com/css2?family=Montserrat:wght@400;500&display=swap">
<style>
  :root {
    --backdrop: #2a2624;
    --card-black: #141414;
    --silver: #bfbfbf;
    --white: #f4f4f4;
    --royal-blue: #2b2f9e;
    --muted: #8a8a8a;
  }
  * { box-sizing: border-box; margin: 0; padding: 0; }
  html, body { width: 1200px; height: 837px; overflow: hidden; }
  body {
    background: var(--backdrop);
    font-family: "Montserrat", Arial, sans-serif;
    display: flex;
    flex-direction: column;
    align-items: center;
    justify-content: center;
    gap: 40px;
  }
  .card {
    width: 640px;
    height: 366px;
    background: var(--card-black);
    border-radius: 6px;
    box-shadow: 0 10px 30px rgba(0,0,0,.45);
    position: relative;
  }
  .brand {
    position: absolute;
    left: 0; right: 0;
    display: flex;
    align-items: center;
    justify-content: center;
    gap: 22px;
  }
  .brand-text { display: flex; flex-direction: column; align-items: flex-end; }
  .brand-name { font-size: 40px; font-weight: 400; letter-spacing: .5px; }
  .brand-tag { font-size: 12px; letter-spacing: 9px; color: var(--muted); margin-top: 6px; margin-right: -9px; }
  .brand-mark { width: 74px; height: 74px; border-radius: 50%; border: 3px solid currentColor; }

  .card-front .brand { top: 140px; }
  .card-front .brand-name, .card-front .brand-mark { color: var(--silver); }

  .card-back .brand { top: 72px; }
  .card-back .brand-name { color: var(--royal-blue); }
  .card-back .brand-mark { color: var(--white); }

  .contact {
    position: absolute;
    left: 0; right: 0; top: 238px;
    display: flex;
    justify-content: center;
    gap: 16px;
    color: var(--white);
    font-size: 15px;
  }
  .contact-col { display: flex; flex-direction: column; gap: 12px; }
  .contact-col.left { align-items: flex-end; }
  .contact-item { display: flex; align-items: center; gap: 8px; }
  .contact-divider { width: 2px; background: var(--royal-blue); }
  .icon {
    width: 20px; height: 20px;
    border-radius: 50%;
    border: 1.5px solid var(--royal-blue);
    display: flex; align-items: center; justify-content: center;
    flex: none;
  }
  .icon svg { width: 11px; height: 11px; fill: none; stroke: var(--white); stroke-width: 2; }
  .icon-plain { width: 8px; height: 8px; border-radius: 50%; background: var(--white); }
</style>
</head>
<body>
  <section class="card card-front" aria-label="Card front">
    <div class="brand">
      <div class="brand-text">
        <span class="brand-name">T. Kellan Studios</span>
        <span class="brand-tag">PHOTOGRAPHY</span>
      </div>
      <span class="brand-mark"></span>
    </div>
  </section>

  <section class="card card-back" aria-label="Card back">
    <div class="brand">
      <div class="brand-text">
        <span class="brand-name">T. Kellan Studios</span>
        <span class="brand-tag">PHOTOGRAPHY</span>
      </div>
      <span class="brand-mark"></span>
    </div>

    <div class="contact">
      <div class="contact-col left">
        <div class="contact-item">
          <span>555-314-8027</span>
          <span class="icon"><svg viewBox="0 0 24 24"><path d="M5 3h4l2 5-3 2a12 12 0 0 0 6 6l2-3 5 2v4a2 2 0 0 1-2 2A18 18 0 0 1 3 5a2 2 0 0 1 2-2z"/></svg></span>
        </div>
        <div class="contact-item">
          <span>info@tkellan-studios.example</span>
          <span class="icon"><svg viewBox="0 0 24 24"><rect x="3" y="6" width="18" height="12"/><path d="M3 6l9 7 9-7"/></svg></span>
        </div>
      </div>
      <div class="contact-divider"></div>
      <div class="contact-col right">
        <div class="contact-item">
          <span class="icon"><span class="icon-plain"></span></span>
          <span>@t.kellanstudios</span>
        </div>
        <div class="contact-item">
          <span class="icon"><svg viewBox="0 0 24 24"><circle cx="12" cy="12" r="9"/><path d="M3 12h18M12 3c3 3 3 15 0 18M12 3c-3 3-3 15 0 18"/></svg></span>
          <span>www.tkellan-studios.example</span>
        </div>
      </div>
    </div>
  </section>
</body>
</html>
```